CloudForge Business Card

I need something that flows with the logo and looks professional but creative. I included the thumbnail file of the photo but will upload the source file once I have it. Colors of business card should flow. I am interested in doing the translucent clear plastic cards as well. My company is called CloudForge in one word and the contact details are below:

Dean Holloway
832-574-2938
www.CloudForgeTx.example
dholloway_47@mailbox.example
Updates

Too much red. I'd rather focus on the blue and put some silver or grey in there.

New Files uploaded. Like the designs so far and am looking forward to seeing more.

Looking for a whole new direction. Let's forget about the plastic card. Let's focus on the blue more than red. I still haven't seen something that really grabs me.

Industry/Entity Type

Plastic

```html
<!DOCTYPE html>
<html lang="en">
<head>
<meta charset="utf-8">
<title>CloudForge Business Card</title>
<link rel="stylesheet" href="https://fonts.googleapis.com/css2?family=Exo+2:wght@400;500;600&display=swap">
<style>
  :root {
    --page: #e4e6e9;
    --card: #ffffff;
    --brand-blue: #1f5fa0;
    --band-blue: #1f5590;
    --stripe-silver: #a9b1ba;
    --name-blue: #1f5fa0;
    --title-grey: #4a4f55;
    --ink-white: #ffffff;
  }
  * { box-sizing: border-box; margin: 0; padding: 0; }
  html, body { width: 1200px; height: 900px; overflow: hidden; }
  body {
    background: var(--page);
    font-family: "Exo 2", sans-serif;
    position: relative;
  }
  .card {
    position: absolute;
    left: 280px;
    width: 640px;
    height: 366px;
    background: var(--card);
    border-radius: 28px;
    overflow: hidden;
    box-shadow: 0 6px 18px rgba(0,0,0,0.12);
  }
  .card--front { top: 60px; }
  .card--back { top: 474px; }
  .card__wave { position: absolute; inset: 0; width: 100%; height: 100%; }
  .brand {
    position: absolute;
    display: flex;
    align-items: center;
    gap: 10px;
    color: var(--brand-blue);
    font-weight: 600;
    letter-spacing: -0.5px;
    line-height: 1;
  }
  .brand__dot {
    width: 14px; height: 14px; border-radius: 50%;
    background: var(--brand-blue);
  }
  .card--front .brand { left: 42px; top: 44px; font-size: 58px; }
  .card--back .brand { left: 0; right: 0; top: 147px; justify-content: center; font-size: 72px; }
  .holder { position: absolute; left: 44px; top: 112px; }
  .holder__name {
    color: var(--name-blue);
    font-size: 19px;
    font-weight: 500;
    line-height: 23px;
    letter-spacing: 1.5px;
    text-transform: uppercase;
  }
  .holder__title {
    color: var(--title-grey);
    font-size: 13px;
    line-height: 16px;
    letter-spacing: 1.2px;
    text-transform: uppercase;
  }
  .address {
    position: absolute; left: 34px; top: 206px;
    color: var(--ink-white);
    font-size: 13px;
    line-height: 21px;
    letter-spacing: 0.8px;
  }
  .contacts {
    position: absolute; right: 30px; top: 272px;
    list-style: none;
    color: var(--ink-white);
    font-size: 11.5px;
    letter-spacing: 0.8px;
  }
  .contacts li {
    display: flex; justify-content: flex-end; align-items: center;
    gap: 8px; height: 16px;
  }
  .contacts svg { width: 11px; height: 11px; flex: none; }
</style>
</head>
<body>
  <section class="card card--front">
    <svg class="card__wave" viewBox="0 0 640 366" aria-hidden="true">
      <path d="M0,188 C120,178 220,190 330,218 S520,268 640,260 L640,366 L0,366 Z" fill="var(--band-blue)"/>
      <path d="M0,176 C120,166 220,178 330,206 S520,256 640,248" fill="none" stroke="var(--stripe-silver)" stroke-width="4"/>
    </svg>
    <div class="brand"><span class="brand__name">CloudForge</span><span class="brand__dot"></span></div>
    <div class="holder">
      <p class="holder__name">Dean Holloway</p>
      <p class="holder__title">Financial Advisor</p>
    </div>
    <p class="address">041.12th floorPlaza<br>Harbor Road LKG</p>
    <ul class="contacts">
      <li>832-574-2938
        <svg viewBox="0 0 12 12"><path d="M3 1 L5 3 L4 5 Q5 7 7 8 L9 7 L11 9 L9 11 Q3 10 1 3 Z" fill="#fff"/></svg></li>
      <li>832-574-2938
        <svg viewBox="0 0 12 12"><rect x="3" y="0.5" width="6" height="11" rx="1" fill="none" stroke="#fff"/></svg></li>
      <li>832-574-2938
        <svg viewBox="0 0 12 12"><rect x="1" y="4" width="10" height="7" fill="#fff"/><rect x="3" y="1" width="6" height="3" fill="none" stroke="#fff"/></svg></li>
      <li>dholloway_47@mailbox.example
        <svg viewBox="0 0 12 12"><rect x="0.5" y="2.5" width="11" height="7" fill="none" stroke="#fff"/><path d="M0.5 2.5 L6 7 L11.5 2.5" fill="none" stroke="#fff"/></svg></li>
      <li>www.CloudForgeTx.example
        <svg viewBox="0 0 12 12"><circle cx="6" cy="6" r="5.2" fill="none" stroke="#fff"/><path d="M1 6 H11 M6 1 V11" stroke="#fff" stroke-width="0.8"/><ellipse cx="6" cy="6" rx="2.3" ry="5.2" fill="none" stroke="#fff" stroke-width="0.8"/></svg></li>
    </ul>
  </section>

  <section class="card card--back">
    <div class="brand"><span class="brand__name">CloudForge</span><span class="brand__dot"></span></div>
  </section>
</body>
</html>
```